Painting Company Business Card

Brightwell Painting needs a new business card. See attachments for our logo and current card as an example.
We want to utilize the same colors in the logo, and keep all the information that is currently on it. Just need an updated and modern design.
We are open to loosing the Association Logos if it means a better design.
We are also entertaining a spot for a picture of a headshot of the person listed on the card. Head shot can be finished later.

```html
<!DOCTYPE html>
<html lang="en">
<head>
<meta charset="UTF-8">
<title>Brightwell Painting – Business Card</title>
<link href="https://fonts.googleapis.com/css2?family=Questrial&display=swap" rel="stylesheet">
<style>
  :root {
    --card-bg: #ffffff;
    --accent-green: #6cd200;
    --brand-green: #2e4220;
    --service-grey: #4f5458;
  }
  html, body {
    margin: 0;
    padding: 0;
    width: 1200px;
    height: 686px;
    overflow: hidden;
    background: var(--card-bg);
  }
  .card {
    position: relative;
    width: 1200px;
    height: 686px;
    background: var(--card-bg);
    font-family: "Questrial", sans-serif;
  }
  .card__bands {
    position: absolute;
    inset: 0;
  }
  .brand-name {
    position: absolute;
    left: 0;
    right: 0;
    top: 88px;
    margin: 0;
    text-align: center;
    color: var(--brand-green);
    font-family: "Questrial", sans-serif;
    font-weight: 400;
    font-size: 112px;
    line-height: 128px;
    letter-spacing: 2px;
  }
  .services {
    position: absolute;
    left: 0;
    right: 0;
    top: 404px;
    margin: 0;
    padding: 0;
    list-style: none;
    text-align: center;
    color: var(--service-grey);
    font-size: 40px;
    line-height: 62px;
  }
</style>
</head>
<body>
  <main class="card">
    <svg class="card__bands" width="1200" height="686" viewBox="0 0 1200 686" aria-hidden="true">
      <polygon class="band band--top" points="309,0 891,0 851,21 354,21" fill="var(--accent-green)"/>
      <rect class="band band--divider" x="0" y="383" width="1200" height="14" fill="var(--accent-green)"/>
      <polygon class="band band--bottom" points="354,663 851,663 891,686 309,686" fill="var(--accent-green)"/>
    </svg>

    <h1 class="brand-name">Brightwell<br>Painting</h1>

    <ul class="services">
      <li class="services__item">-&gt; Exterior Painting &lt;-</li>
      <li class="services__item">-&gt; Interior Painting &lt;-</li>
      <li class="services__item">-&gt; Carpentry &lt;-</li>
      <li class="services__item">-&gt; Drywall &lt;-</li>
    </ul>
  </main>
</body>
</html>
```